Harborline Energy - needs a business card

Harborline Energy is a U.S. based diesel sourcing and distribution company that supports American oil & gas fields through providing quality product and consistent services.

Target Market(s)

Oil and Gas

Contact Information for Business Card

The background of the card must be white to ensure the logo pops.

Font styles to use
Serif
Sans Serif

Colors

Designer to choose colors to be used in the design.

Requirements
Must have
• Front of Card: Tag line: Harborline Energy, Powering America's Oil & Gas fields.
• Not sure if you guys do this part but just in case...
• Dale Menschow
• Owner/CEO
• C:555.318.4076
• E:Dmenschow@harborlineenergy.example
• W:Harborlineenergy.example
• Locations: Servicing the Powder River, DJ basin and Bakken formations.
• Back of Card: " Frac fueling is what we do. We understand how important diesel fuel is to your operation, which is why our main service line is Frac fueling. We assure our supply and stand by our service"

```html
<!DOCTYPE html>
<html lang="en">
<head>
<meta charset="utf-8">
<title>Harborline Energy – Business Card</title>
<link rel="stylesheet" href="https://fonts.googleapis.com/css2?family=Open+Sans:wght@700&family=Roboto+Condensed:wght@400&family=Roboto:wght@400&display=swap">
<style>
  :root {
    --navy: #002a5c;
    --navy-mid: #0a3570;
    --black: #000000;
    --white: #ffffff;
    --red: #b40f14;
    --ink: #111111;
    --detail-ink: #dde5f0;
    --stage-light: #ececec;
    --stage-dark: #8a8a8a;
  }
  html, body {
    margin: 0;
    padding: 0;
    width: 1200px;
    height: 1200px;
    overflow: hidden;
  }
  body {
    background: radial-gradient(ellipse at center, var(--stage-dark) 0%, #b5b5b5 55%, var(--stage-light) 100%);
    position: relative;
    font-family: "Roboto", sans-serif;
  }
  .card {
    position: absolute;
    left: 103px;
    width: 999px;
    height: 499px;
    overflow: hidden;
    box-shadow: 0 6px 40px rgba(0,0,0,0.45);
  }
  .card--front { top: 22px; background: var(--white); }
  .card--back  { top: 626px; background: var(--navy); }
  .card__shapes {
    position: absolute;
    inset: 0;
    width: 100%;
    height: 100%;
  }

  /* Front */
  .front__title {
    position: absolute;
    left: 0;
    width: 602px;
    top: 14px;
    text-align: center;
    color: var(--white);
    font-size: 36px;
    line-height: 1.2;
  }
  .front__details {
    position: absolute;
    left: 0;
    top: 0;
    color: var(--detail-ink);
    font-family: "Roboto Condensed", sans-serif;
  }
  .detail {
    position: absolute;
    white-space: nowrap;
    font-size: 28px;
    line-height: 1;
  }
  .detail__label { position: absolute; left: 0; }
  .detail__eq { position: absolute; left: 108px; }
  .detail__value { position: absolute; left: 135px; }
  .detail--name { font-size: 38px; left: 42px; top: 118px; }
  .detail--name .detail__eq { left: 88px; }
  .detail--name .detail__value { left: 121px; }
  .detail--contact { left: 17px; top: 192px; }
  .detail--email { left: 24px; top: 245px; }
  .detail--email .detail__value { font-size: 22px; top: 4px; left: 128px; }
  .detail--web { left: 30px; top: 295px; }
  .detail--web .detail__eq { left: 102px; }
  .detail--web .detail__value { left: 134px; }
  .detail--locations { left: 24px; top: 364px; font-size: 22px; line-height: 28px; }
  .detail--locations .detail__eq { left: 101px; }
  .detail--locations .detail__value { left: 133px; }
  .detail--locations .detail__value span { display: block; }
  .detail--locations .detail__value span + span { margin-left: -4px; }

  .front__brand {
    position: absolute;
    left: 600px;
    width: 390px;
    top: 200px;
    display: flex;
    align-items: center;
    justify-content: center;
    gap: 14px;
    color: var(--navy);
    font-family: "Open Sans", sans-serif;
    font-weight: 700;
    font-size: 34px;
  }
  .brand__dot {
    width: 26px;
    height: 26px;
    border-radius: 50%;
    background: var(--red);
    flex: none;
  }
  .front__tagline {
    position: absolute;
    right: 22px;
    top: 434px;
    color: var(--ink);
    font-size: 30px;
    white-space: nowrap;
  }

  /* Back */
  .back__message {
    position: absolute;
    left: 0;
    width: 999px;
    top: 62px;
    text-align: center;
    color: var(--white);
    font-family: "Open Sans", sans-serif;
    font-weight: 700;
    font-size: 31px;
    line-height: 1.2;
  }
  .back__message p { margin: 0; }
  .back__lead { margin-bottom: 44px !important; }
  .back__brand {
    position: absolute;
    left: 24px;
    top: 410px;
    color: var(--navy-mid);
    font-family: "Open Sans", sans-serif;
    font-weight: 700;
    font-size: 32px;
  }
</style>
</head>
<body>

<section class="card card--front" aria-label="Business card front">
  <svg class="card__shapes" viewBox="0 0 999 499" preserveAspectRatio="none" aria-hidden="true">
    <defs>
      <linearGradient id="edge-shade" x1="0" y1="0" x2="1" y2="0">
        <stop offset="0" stop-color="#000" stop-opacity="0.25"/>
        <stop offset="1" stop-color="#000" stop-opacity="0"/>
      </linearGradient>
    </defs>
    <polygon points="0,0 690,0 450,499 0,499" fill="url(#edge-shade)" transform="translate(14,0)"/>
    <polygon class="front__panel" points="0,0 690,0 450,499 0,499" fill="#002a5c"/>
    <polygon class="front__header" points="0,0 690,0 646,73 0,73" fill="#000"/>
    <polygon class="front__corner" points="888,0 999,0 999,73" fill="#b40f14"/>
  </svg>

  <div class="front__title">Harborline Energy</div>

  <div class="front__details">
    <div class="detail detail--name">
      <span class="detail__label">CEO</span><span class="detail__eq">=</span><span class="detail__value">Dale Menschow</span>
    </div>
    <div class="detail detail--contact">
      <span class="detail__label">contact</span><span class="detail__eq">=</span><span class="detail__value">555.318.4076</span>
    </div>
    <div class="detail detail--email">
      <span class="detail__label">Email</span><span class="detail__eq">=</span><span class="detail__value">Dmenschow@harborlineenergy.example</span>
    </div>
    <div class="detail detail--web">
      <span class="detail__label">web</span><span class="detail__eq">=</span><span class="detail__value">Harborlineenergy.example</span>
    </div>
    <div class="detail detail--locations">
      <span class="detail__label">Locations</span><span class="detail__eq">=</span>
      <span class="detail__value"><span>Servicing the Powder River,</span><span>DJ basin and Bakken formations.</span></span>
    </div>
  </div>

  <div class="front__brand"><span class="brand__dot"></span>Harborline Energy</div>

  <div class="front__tagline">Powering America's Oil &amp; Gas fields</div>
</section>

<section class="card card--back" aria-label="Business card back">
  <svg class="card__shapes" viewBox="0 0 999 499" preserveAspectRatio="none" aria-hidden="true">
    <defs>
      <linearGradient id="back-shade" x1="0" y1="0" x2="1" y2="0">
        <stop offset="0" stop-color="#000" stop-opacity="0.8"/>
        <stop offset="1" stop-color="#000" stop-opacity="0"/>
      </linearGradient>
    </defs>
    <polygon points="0,0 520,0 272,499 0,499" fill="url(#back-shade)" transform="translate(40,0)"/>
    <polygon class="back__dark" points="0,0 520,0 272,499 0,499" fill="#000"/>
    <polygon class="back__light" points="999,240 999,499 557,499" fill="#fff"/>
  </svg>

  <div class="back__brand">Harborline Energy</div>

  <div class="back__message">
    <p class="back__lead">Frac fueling is what we do</p>
    <p>We understand how important diesel fuel is to your operation,</p>
    <p>which is why our main service line is Frac fueling</p>
    <p>We assure our supply and stand by our service"</p>
  </div>
</section>

</body>
</html>
```